New Construction company looking for powerful bold logo. people see the logo, leaves an impression

We need a business card for our new company. We provide site work for commercial projects in South Texas. We clear land, excavation, run under ground utilities, concrete work, dirt work etc. We like the black card. I created a webpage www.tarn-vbuilders.com .... As I grow with projects I will put up pictures with video, and intro music. Want it look cool, bold, powerful, and slick looking. Creating 'TVB'....as my logo (possibly or if you have something you want to have fun with). Just have fun!!....thank you!

Dorian Pruett Business Manager Serving South Texas PO Box 4837 Robstown,TX. 78380 Mobile: 361-752-6083 www.tarn-vbuilders.com dorian@tarn-vbuilders.com you can put this anyway you see fit in your design and layout. thank you

Target Market(s)

General Contractors; Home Builders;

Industry/Entity Type

Construction

Contact Information for Business Card

I want the card to be black.

Font styles to use
Other font styles liked:
• Designer choice

Requirements
Must have
• Tarn-V Construction
• Site Work - Utilities/Concrete/Pad/Grading/Excavation (on the back side)
Nice to have
• Maybe TVB as the logo.....or just a symbol that would be TV.....and then construction to tie it togther...

```html
<!DOCTYPE html>
<html lang="en">
<head>
<meta charset="utf-8">
<title>Tarn-V Construction — Business Card</title>
<link href="https://fonts.googleapis.com/css2?family=Lato:wght@400;700;900&display=swap" rel="stylesheet">
<style>
  :root {
    --page: #d9d9d6;
    --card: #151515;
    --card-edge: #1e1e1e;
    --yellow: #fde21c;
    --yellow-soft: #f8c83a;
    --ink: #111111;
    --text: #e9e9e9;
  }
  * { margin: 0; padding: 0; box-sizing: border-box; }
  html, body { width: 1200px; height: 900px; overflow: hidden; }
  body {
    background: var(--page);
    font-family: "Lato", Arial, sans-serif;
    position: relative;
  }
  .card {
    position: absolute;
    left: 267px;
    width: 666px;
    height: 380px;
    background: linear-gradient(135deg, var(--card-edge), var(--card) 60%);
    border-radius: 18px;
    overflow: hidden;
    box-shadow: 0 10px 30px rgba(0,0,0,.25);
  }
  .card--back { top: 50px; }
  .card--front { top: 470px; }

  /* company name set as plain text in place of the mark */
  .brand-name {
    position: absolute;
    color: var(--yellow);
    font-weight: 900;
    line-height: 1.05;
    white-space: nowrap;
  }
  .card--back .brand-name {
    left: 0; right: 0;
    top: 120px;
    text-align: center;
    font-size: 34px;
  }
  .card--front .brand-name {
    left: 40px;
    top: 138px;
    width: 290px;
    font-size: 44px;
  }

  .services {
    position: absolute;
    left: 0; right: 0;
    top: 228px;
    height: 40px;
    background: var(--yellow);
    display: flex;
    justify-content: center;
    align-items: center;
    gap: 30px;
    list-style: none;
  }
  .services__item {
    display: flex;
    align-items: center;
    gap: 8px;
    color: var(--ink);
    font-weight: 900;
    font-size: 17px;
    text-transform: uppercase;
  }
  .services__item::before {
    content: "";
    width: 8px; height: 8px;
    background: var(--ink);
  }

  .name-band {
    position: absolute;
    right: 0;
    top: 58px;
    width: 310px;
    height: 52px;
    background: var(--yellow);
    padding: 8px 0 0 22px;
    color: var(--ink);
  }
  .name-band::after {
    content: "";
    position: absolute;
    right: 0; top: 0;
    width: 34px; height: 100%;
    background: var(--yellow-soft);
  }
  .name-band__name { font-size: 21px; line-height: 1; text-transform: uppercase; }
  .name-band__name strong { font-weight: 900; }
  .name-band__name span { font-weight: 400; }
  .name-band__role { font-size: 12px; margin-top: 3px; }

  .contact {
    position: absolute;
    left: 376px;
    top: 140px;
    list-style: none;
    color: var(--text);
    font-size: 14px;
  }
  .contact__row { display: flex; gap: 10px; margin-bottom: 6px; line-height: 1.3; }
  .contact__row--address { margin-bottom: 12px; }
  .contact__tag {
    flex: none;
    width: 15px; height: 15px;
    margin-top: 2px;
    background: var(--yellow);
    color: var(--ink);
    font-size: 10px;
    font-weight: 700;
    display: flex;
    align-items: center;
    justify-content: center;
  }
</style>
</head>
<body>

<section class="card card--back" aria-label="Card back">
  <p class="brand-name">Tarn-V Construction</p>
  <ul class="services">
    <li class="services__item">Pad</li>
    <li class="services__item">Concrete</li>
    <li class="services__item">Utilities</li>
    <li class="services__item">Grading</li>
    <li class="services__item">Excavation</li>
  </ul>
</section>

<section class="card card--front" aria-label="Card front">
  <p class="brand-name">Tarn-V<br>Construction</p>

  <div class="name-band">
    <p class="name-band__name"><strong>Dorian</strong> <span>Pruett</span></p>
    <p class="name-band__role">Managing Director</p>
  </div>

  <ul class="contact">
    <li class="contact__row contact__row--address"><span class="contact__tag">A</span><span>PO Box 4837,<br>Robstown TX 78380</span></li>
    <li class="contact__row"><span class="contact__tag">P</span><span>361 . 752 . 6083</span></li>
    <li class="contact__row"><span class="contact__tag">E</span><span>dorian@tarn-vbuilders.com</span></li>
    <li class="contact__row"><span class="contact__tag">W</span><span>www.tarn-vbuilders.com</span></li>
  </ul>
</section>

</body>
</html>
```